Corvel Power renewable energy company Website design

Re-design our current website www.corvelpower.com.au. Products and packages need updating which we can provide. Just looking for a change from our tired website. Would like to add a blog section to the website along with EV Chargers section. Need to add our QLD electrical contractors licence number to each footer on every page. Need to keep the get a quote form fill section.

Target Market(s)

Home owners looking for renewable energy options

Industry/Entity Type

Renewable Energy

Coding

Coded - Design and coding required

Number of Pages Required

5+ page

Requirements
Nice to have
• We do like a website that flows and has movement. In a way directing the consumers eyes to which ever section we want highlighted.

```html
<!DOCTYPE html>
<html lang="en">
<head>
<meta charset="utf-8">
<title>Corvel Power — Solar Power Solutions</title>
<link href="https://fonts.googleapis.com/css2?family=Poppins:wght@400;500;600;700;800&display=swap" rel="stylesheet">
<style>
:root{
  --red:#c8102e;
  --red-dark:#a00c24;
  --ink:#1d1d1f;
  --text:#555a60;
  --muted:#8a8f95;
  --line:#e3e5e8;
  --grey-band:#f1f2f4;
  --white:#ffffff;
  --footer:#1b1c20;
}
*{box-sizing:border-box;margin:0;padding:0}
html,body{width:1200px;height:3752px;overflow:hidden}
body{font-family:"Poppins",Arial,sans-serif;color:var(--ink);background:var(--white);position:relative}
.abs{position:absolute}
.btn{display:inline-block;background:var(--red);color:#fff;font-size:11px;font-weight:600;letter-spacing:.5px;padding:10px 20px;text-transform:uppercase}

/* hero */
.hero{position:absolute;left:0;top:0;width:1200px;height:560px;overflow:hidden}
.hero-photo{position:absolute;inset:0;background:linear-gradient(180deg,#6fa6d6 0%,#a9cbe6 38%,#8d9aa6 62%,#5f6f5a 100%)}
.hero-roof{position:absolute;right:0;top:150px;width:760px;height:410px;background:linear-gradient(160deg,#c7ccd1,#8d959c);clip-path:polygon(30% 0,100% 0,100% 100%,0 100%)}
.hero-cut{position:absolute;left:0;bottom:0;width:1200px;height:120px;background:#fff;clip-path:polygon(0 100%,100% 18%,100% 100%)}
.hero-cut-red{position:absolute;left:0;bottom:0;width:1200px;height:124px;background:var(--red);clip-path:polygon(60% 100%,100% 14%,100% 18%,62% 100%)}
.nav{position:absolute;left:0;top:0;width:1200px;height:56px;display:flex;align-items:center;padding:0 160px}
.brand{display:flex;align-items:center;gap:8px;color:#fff;font-weight:700;font-size:15px;background:var(--red);padding:8px 12px}
.brand-mark{width:12px;height:12px;background:#fff}
.menu{margin-left:auto;display:flex;gap:26px;font-size:11px;font-weight:500;color:#fff}
.menu .active{color:var(--red);border-bottom:2px solid var(--red);padding-bottom:2px}
.hero-title{position:absolute;left:160px;top:62px;font-size:92px;font-weight:800;color:#fff;line-height:1;letter-spacing:-1px}
.hero-sub{position:absolute;left:164px;top:166px;font-size:26px;font-weight:500;color:#fff}
.hero .btn{position:absolute;left:164px;top:218px}

/* difference */
.section-title{font-size:38px;font-weight:700;text-align:center}
.difference-title{position:absolute;top:578px;left:0;width:1200px}
.difference-card{position:absolute;left:220px;top:640px;width:760px;height:200px;background:#fff;box-shadow:0 10px 30px rgba(0,0,0,.12);display:flex;justify-content:space-around;align-items:flex-start;padding-top:42px;border-bottom:4px solid var(--red)}
.feature{width:110px;text-align:center;font-size:10px;line-height:1.4;color:var(--text)}
.feature-icon{width:48px;height:48px;border:1.5px solid var(--muted);border-radius:50%;margin:0 auto 12px;display:flex;align-items:center;justify-content:center}

/* solution */
.solution-frame{position:absolute;left:180px;top:900px;width:480px;height:420px;border-left:4px solid var(--red);border-top:4px solid var(--red)}
.solution-photo{position:absolute;left:196px;top:916px;width:464px;height:404px;background:linear-gradient(180deg,#b9d3ea 0%,#dfe6ec 45%,#8c9a7e 75%,#5e7353 100%)}
.solution-text{position:absolute;left:672px;top:948px;width:360px}
.solution-text h2{font-size:38px;font-weight:700;margin-bottom:14px}
.solution-text p{font-size:11px;line-height:1.7;color:var(--text);margin-bottom:12px}

/* packages */
.packages{position:absolute;left:0;top:1380px;width:1200px;height:620px;background:var(--grey-band)}
.packages .section-title{position:absolute;top:42px;width:1200px}
.package{position:absolute;top:120px;width:290px;height:470px;background:#fff;box-shadow:0 6px 18px rgba(0,0,0,.08)}
.package-badge{position:absolute;left:16px;top:16px;width:56px;height:56px;border-radius:50%;background:var(--red);color:#fff;font-size:10px;font-weight:700;display:flex;align-items:center;justify-content:center;text-align:center;line-height:1.1}
.package-partner{position:absolute;right:26px;top:34px;width:70px;height:18px;background:#3c9b3c;border-radius:3px}
.package-product{position:absolute;left:60px;top:70px;width:170px;height:150px;background:linear-gradient(135deg,#2a2f3a,#111521);border:3px solid #c9ccd1}
.package-inverter{position:absolute;left:40px;top:180px;width:70px;height:60px;background:linear-gradient(180deg,#f3f4f6,#cfd3d8);border-radius:4px}
.package-from{position:absolute;top:262px;width:290px;text-align:center;font-size:10px;color:var(--muted)}
.package-price{position:absolute;top:274px;width:290px;text-align:center;font-size:32px;font-weight:700;color:var(--red)}
.package-list{position:absolute;left:40px;top:332px;list-style:none;font-size:10px;color:var(--text)}
.package-list li{display:flex;align-items:center;gap:8px;margin-bottom:10px}
.dot{width:12px;height:12px;border-radius:50%;border:1.5px solid var(--red);flex:none}
.package-bar{position:absolute;left:0;bottom:0;width:290px;height:8px;background:var(--red)}

/* savings */
.savings-text{position:absolute;left:208px;top:2060px;width:380px}
.savings-text h2{font-size:44px;font-weight:700;line-height:1.1;margin-bottom:18px}
.savings-text p{font-size:11px;line-height:1.7;color:var(--text);margin-bottom:12px}
.savings-text .btn{margin-top:10px}
.diamond-tile{position:absolute;width:150px;height:150px;background:var(--red);transform:rotate(45deg);box-shadow:0 8px 20px rgba(200,16,46,.25)}
.diamond-label{position:absolute;width:120px;text-align:center;color:#fff;font-size:10px;font-weight:600;line-height:1.3}
.diamond-core{position:absolute;left:854px;top:2238px;width:52px;height:52px;background:#fff;transform:rotate(45deg);border:3px solid var(--red)}

/* partners */
.partners{position:absolute;left:0;top:2520px;width:1200px;height:360px;background:var(--grey-band)}
.partner{position:absolute;width:160px;height:70px;background:#fff;border:1px solid var(--line);display:flex;align-items:center;justify-content:center}
.partner span{display:block;width:100px;height:18px;border-radius:3px}

/* contact */
.contact-text{position:absolute;left:160px;top:2915px;width:420px}
.contact-text h2{font-size:38px;font-weight:700;margin-bottom:18px}
.contact-row{display:flex;gap:40px;font-size:11px;color:var(--text);margin-bottom:14px}
.contact-item{display:flex;align-items:center;gap:8px}
.contact-icon{width:26px;height:26px;border-radius:50%;background:var(--red);display:flex;align-items:center;justify-content:center}
.quote-label{font-size:11px;font-weight:600;margin:22px 0 14px}
.field-grid{display:grid;grid-template-columns:1fr 1fr;gap:10px}
.field{height:34px;border:1px solid var(--line);font-size:10px;color:var(--muted);padding:10px}
.field.message{grid-column:1 / 3;height:100px}
.contact-text .btn{margin-top:14px}
.contact-photo{position:absolute;left:600px;top:2890px;width:600px;height:630px;background:linear-gradient(180deg,#5e8fc1 0%,#b8cde0 40%,#c9a27a 70%,#3b4f3c 100%)}

/* footer */
.footer{position:absolute;left:0;top:3520px;width:1200px;height:232px;background:var(--footer);color:#c7c9cc}
.footer .brand{position:absolute;left:160px;top:40px}
.footer-col{position:absolute;top:40px;font-size:10px;line-height:2}
.footer-col h4{color:#fff;font-size:12px;font-weight:600;margin-bottom:6px}
.footer-copy{position:absolute;left:0;bottom:0;width:1200px;height:40px;border-top:1px solid #2f3036;text-align:center;font-size:9px;line-height:40px;color:#8a8c90}
</style>
</head>
<body>

<header class="hero">
  <div class="hero-photo" role="img" aria-label="Blue sky over hills with solar installers fitting panels on a metal roof"></div>
  <div class="hero-roof" role="img" aria-label="Metal roof with solar panels"></div>
  <nav class="nav">
    <div class="brand"><span class="brand-mark"></span>Corvel Power</div>
    <div class="menu">
      <span class="active">About Us</span><span>Products</span><span>Inverters</span><span>Panels</span><span>Residential</span><span>Batteries</span><span>Commercial</span><span>Blog</span><span>EV Charger</span><span>Faq</span>
    </div>
  </nav>
  <h1 class="hero-title">Australia's</h1>
  <p class="hero-sub">Top provider of solar power solutions</p>
  <span class="btn">Learn More</span>
  <div class="hero-cut-red"></div>
  <div class="hero-cut"></div>
</header>

<h2 class="section-title difference-title">The Difference</h2>
<section class="difference-card">
  <div class="feature"><div class="feature-icon"><svg width="20" height="24" viewBox="0 0 20 24"><path d="M10 1a8 8 0 0 0-8 8c0 6 8 14 8 14s8-8 8-14a8 8 0 0 0-8-8z" fill="none" stroke="#c8102e" stroke-width="1.6"/><circle cx="10" cy="9" r="3" fill="#c8102e"/></svg></div>Local Business</div>
  <div class="feature"><div class="feature-icon"><svg width="24" height="24" viewBox="0 0 24 24"><path d="M12 2l3 6.5 7 .8-5.2 4.8 1.5 7L12 17.5 5.7 21l1.5-7L2 9.3l7-.8z" fill="none" stroke="#c8102e" stroke-width="1.6"/></svg></div>5 Star Customer Reviews</div>
  <div class="feature"><div class="feature-icon"><svg width="24" height="24" viewBox="0 0 24 24"><rect x="3" y="4" width="18" height="14" fill="none" stroke="#c8102e" stroke-width="1.6"/><path d="M8 11l3 3 5-6" fill="none" stroke="#c8102e" stroke-width="1.6"/></svg></div>Our Own Certified Skilled Installation Teams</div>
  <div class="feature"><div class="feature-icon"><svg width="24" height="24" viewBox="0 0 24 24"><path d="M12 2l8 3v6c0 5-4 9-8 11-4-2-8-6-8-11V5z" fill="none" stroke="#c8102e" stroke-width="1.6"/></svg></div>Work Leading Brands Minimum 10 Year Warranty</div>
  <div class="feature"><div class="feature-icon"><svg width="24" height="24" viewBox="0 0 24 24"><path d="M4 13a8 8 0 0 1 16 0v5h-4v-6h4M4 12h4v6H4z" fill="none" stroke="#c8102e" stroke-width="1.6"/></svg></div>Responsive and Great Quality Customer Service</div>
</section>

<div class="solution-frame"></div>
<div class="solution-photo" role="img" aria-label="Modern two-storey home with solar panels on the roof and a green lawn"></div>
<section class="solution-text">
  <h2>Solution</h2>
  <p>We understand that every home and business has different energy requirements. This is why we implement a collaborative approach and customise a package to align with your energy goals.</p>
  <p>Our sound installations validate the relations between your consideration, including geography and conditions, the best quality and your financial budget. You can be confident in your choice and in a team dedicated to you, with a long lasting system.</p>
  <span class="btn">Learn More</span>
</section>

<section class="packages">
  <h2 class="section-title">Packages</h2>

  <article class="package" style="left:152px">
    <div class="package-badge">6.6kW<br>System</div>
    <div class="package-partner"></div>
    <div class="package-product" role="img" aria-label="Black solar panel"></div>
    <div class="package-inverter" role="img" aria-label="White solar inverter"></div>
    <div class="package-from">From</div>
    <div class="package-price">$5999</div>
    <ul class="package-list">
      <li><span class="dot"></span>Includes 6.6kW of N-Type Panels</li>
      <li><span class="dot"></span>5kW Single Phase Inverter</li>
      <li><span class="dot"></span>What $5999 Gets You</li>
    </ul>
    <div class="package-bar"></div>
  </article>

  <article class="package" style="left:455px">
    <div class="package-badge">6.6kW<br>System</div>
    <div class="package-partner"></div>
    <div class="package-product" role="img" aria-label="Black solar panel"></div>
    <div class="package-inverter" role="img" aria-label="White solar inverter"></div>
    <div class="package-from">From</div>
    <div class="package-price">$3999</div>
    <ul class="package-list">
      <li><span class="dot"></span>Includes 6.6kW of Mono Panels</li>
      <li><span class="dot"></span>5kW Single Phase Inverter</li>
      <li><span class="dot"></span>What $3999 Gets You</li>
    </ul>
    <div class="package-bar"></div>
  </article>

  <article class="package" style="left:758px">
    <div class="package-badge">10kW<br>System</div>
    <div class="package-partner"></div>
    <div class="package-product" role="img" aria-label="Black solar panel"></div>
    <div class="package-inverter" role="img" aria-label="White solar inverter"></div>
    <div class="package-from">From</div>
    <div class="package-price">$6400</div>
    <ul class="package-list">
      <li><span class="dot"></span>Includes 10kW of N-Type Panels</li>
      <li><span class="dot"></span>8kW Three Phase Inverter</li>
      <li><span class="dot"></span>What $6400 Gets You</li>
    </ul>
    <div class="package-bar"></div>
  </article>
</section>

<section class="savings-text">
  <h2>Watch Your<br>Savings Grow.</h2>
  <p>With growing electricity costs, both homeowners and businesses are feeling the pressure. Harnessing renewable energy with solar is one of the most effective ways to cut household energy costs.</p>
  <p>We'll provide you with an energy system you'll love that will pay for itself fast. Reliable systems and support for years so you can enjoy clean power and lower bills well into the future.</p>
  <span class="btn">Learn More</span>
</section>

<div class="diamond-tile" style="left:805px;top:2080px"></div>
<div class="diamond-tile" style="left:700px;top:2188px"></div>
<div class="diamond-tile" style="left:910px;top:2188px"></div>
<div class="diamond-tile" style="left:805px;top:2296px"></div>
<div class="diamond-core"></div>
<div class="diamond-label" style="left:820px;top:2140px">Reduce carbon, grow your business</div>
<div class="diamond-label" style="left:715px;top:2250px">Boost value for your home</div>
<div class="diamond-label" style="left:925px;top:2250px">Cut energy bills with solar</div>
<div class="diamond-label" style="left:820px;top:2358px">Go solar, save on power bills</div>

<section class="partners" aria-label="Partner brands">
  <div class="partner" style="left:160px;top:50px"><span style="background:#e8a11b"></span></div>
  <div class="partner" style="left:340px;top:50px"><span style="background:#b9bcc1"></span></div>
  <div class="partner" style="left:520px;top:50px"><span style="background:#9bb6d8"></span></div>
  <div class="partner" style="left:700px;top:50px"><span style="background:#6c6f74"></span></div>
  <div class="partner" style="left:880px;top:50px"><span style="background:#c5c8cc"></span></div>
  <div class="partner" style="left:160px;top:150px"><span style="background:#a7aaae"></span></div>
  <div class="partner" style="left:340px;top:150px"><span style="background:#bfc3c7"></span></div>
  <div class="partner" style="left:520px;top:150px"><span style="background:#c9ccd0"></span></div>
  <div class="partner" style="left:700px;top:150px"><span style="background:#7d8186"></span></div>
  <div class="partner" style="left:880px;top:150px"><span style="background:#d0d3d6"></span></div>
  <div class="partner" style="left:340px;top:250px"><span style="background:#2e6cb5"></span></div>
  <div class="partner" style="left:520px;top:250px"><span style="background:#d3d6d9"></span></div>
</section>

<section class="contact-text">
  <h2>Contact us</h2>
  <div class="contact-row">
    <div class="contact-item"><span class="contact-icon"><svg width="12" height="12" viewBox="0 0 24 24"><path d="M6 2l4 4-2 3c1 3 4 6 7 7l3-2 4 4-3 4C10 22 2 14 2 5z" fill="#fff"/></svg></span>(07) 5550 1824</div>
    <div class="contact-item"><span class="contact-icon"><svg width="12" height="12" viewBox="0 0 24 24"><rect x="2" y="5" width="20" height="14" fill="#fff"/><path d="M2 5l10 8 10-8" fill="none" stroke="#c8102e" stroke-width="2"/></svg></span>info@corvelpower.com.au</div>
  </div>
  <div class="contact-row">
    <div class="contact-item"><span class="contact-icon"><svg width="12" height="12" viewBox="0 0 24 24"><path d="M12 1a8 8 0 0 0-8 8c0 6 8 14 8 14s8-8 8-14a8 8 0 0 0-8-8z" fill="#fff"/></svg></span>12 Harbour Lane, Brisbane QLD 4000</div>
  </div>
  <p class="quote-label">GET IN TOUCH FOR AN OBLIGATION FREE QUOTE.</p>
  <div class="field-grid">
    <div class="field">Name</div>
    <div class="field">Phone</div>
    <div class="field">Email address</div>
    <div class="field">Suburb</div>
    <div class="field">Address</div>
    <div class="field">Postcode</div>
    <div class="field message">Message</div>
  </div>
  <span class="btn">Submit</span>
</section>
<div class="contact-photo" role="img" aria-label="Modern home with large glass windows lit at dusk"></div>

<footer class="footer">
  <div class="brand"><span class="brand-mark"></span>Corvel Power</div>
  <div class="footer-col" style="left:470px"><h4>COMPANY</h4>About Us<br>Residential<br>Commercial</div>
  <div class="footer-col" style="left:650px"><h4>ABOUT US</h4>(07) 5550 1824<br>info@corvelpower.com.au</div>
  <div class="footer-col" style="left:860px"><h4>LICENSE</h4>QLD Electrical Contractors Licence 12345</div>
  <div class="footer-copy">© 2024 Corvel Power. All rights reserved.</div>
</footer>

</body>
</html>
```